I would like a formal monogram with LM and Lorna Mabbery Interiors written somehow. this a a new interior design company based in Dallas. My favorite colors is Halvorne blue with gold or white writing or some variation of.
back: Lorna Mabbery
214-630-4182
lorna.mabbery@quillpost.example
www.lornamabberyinteriors.example

```html
<!DOCTYPE html>
<html lang="en">
<head>
<meta charset="utf-8">
<title>Lorna Mabbery Interiors — Business Card</title>
<link rel="stylesheet" href="https://fonts.googleapis.com/css2?family=Marcellus&family=Montserrat:wght@300&family=Roboto:wght@300&display=swap">
<style>
  :root {
    --backdrop: #2a2a2a;
    --card-dark: #1e1f20;
    --card-dark-edge: #2a2b2c;
    --teal: #0fa3a3;
    --teal-deep: #0a8f90;
    --gold: #c9a045;
    --gold-light: #e6c266;
    --gold-dark: #9a7228;
    --ink-light: #d8d8d8;
    --white: #f4f4f4;
  }
  * { box-sizing: border-box; margin: 0; padding: 0; }
  html, body {
    width: 1200px; height: 1138px; overflow: hidden;
    background: var(--backdrop);
  }
  .card {
    position: absolute; left: 273px; width: 620px; height: 376px;
    border-radius: 16px; overflow: hidden;
    background: linear-gradient(160deg, var(--card-dark) 0%, var(--card-dark-edge) 100%);
    box-shadow: 0 6px 14px rgba(0,0,0,0.45);
  }
  .card--front { top: 184px; }
  .card--back { top: 606px; }

  .mark-ring {
    position: absolute; border-radius: 50%;
    border: 3px solid var(--gold);
  }
  .card--front .mark-ring { left: 280px; top: 88px; width: 94px; height: 94px; }
  .card--back .mark-ring { left: 98px; top: 144px; width: 118px; height: 118px; }

  .wordmark {
    position: absolute; text-align: center; font-weight: 400;
  }
  .wordmark__name {
    display: block; white-space: nowrap; line-height: 1;
    font-family: "Marcellus", serif; color: var(--teal);
  }
  .wordmark__sub {
    display: block; white-space: nowrap; line-height: 1;
    font-family: "Montserrat", sans-serif; font-weight: 300; color: var(--ink-light);
  }
  .card--front .wordmark { top: 192px; left: 0; width: 100%; }
  .card--front .wordmark__name { font-size: 50px; letter-spacing: 2px; }
  .card--front .wordmark__sub { font-size: 22px; letter-spacing: 37px; padding-left: 37px; margin-top: 14px; }

  .site-line {
    position: absolute; top: 335px; left: 0; width: 100%;
    display: flex; align-items: center; justify-content: center; gap: 16px;
    font-family: "Roboto", sans-serif; font-weight: 300; font-size: 16px; line-height: 20px; color: var(--ink-light);
  }
  .site-line__rule { width: 86px; height: 2px; background: linear-gradient(90deg, transparent, var(--gold)); }
  .site-line__rule--right { background: linear-gradient(90deg, var(--gold), transparent); }

  .front-band {
    position: absolute; left: 0; bottom: 0; width: 100%; height: 11px; display: flex;
  }
  .front-band__teal { flex: 1; background: var(--teal-deep); }
  .front-band__gold { flex: 1; background: linear-gradient(90deg, var(--gold-dark), var(--gold-light) 40%, var(--gold-dark)); }

  .back-sweep {
    position: absolute; left: 0; top: 0; width: 100%; height: 146px;
    background: linear-gradient(100deg, var(--card-dark) 0%, var(--card-dark) 28%, #6e5626 40%, var(--gold-dark) 48%, var(--teal-deep) 62%, var(--teal) 100%);
  }

  .back-name {
    position: absolute; right: 32px; top: 30px; text-align: right; font-weight: 400;
    font-family: "Marcellus", serif; font-size: 29px; line-height: 30px; color: var(--white);
  }

  .card--back .wordmark { top: 284px; left: 26px; width: 254px; }
  .card--back .wordmark__name { font-size: 29px; }
  .card--back .wordmark__sub { font-size: 13px; letter-spacing: 20px; padding-left: 20px; margin-top: 8px; }

  .contact {
    position: absolute; right: 33px; top: 260px; list-style: none;
    font-family: "Roboto", sans-serif; font-weight: 300; font-size: 16px; color: var(--ink-light);
  }
  .contact__item { display: flex; align-items: center; justify-content: flex-end; gap: 12px; height: 24px; }
  .contact__icon { width: 14px; height: 14px; flex: none; }
</style>
</head>
<body>

<section class="card card--front" aria-label="Card front">
  <span class="mark-ring" aria-hidden="true"></span>
  <h1 class="wordmark">
    <span class="wordmark__name">LORNA MABBERY</span>
    <span class="wordmark__sub">INTERIORS</span>
  </h1>
  <p class="site-line">
    <span class="site-line__rule"></span>
    <span>www.lornamabberyinteriors.example</span>
    <span class="site-line__rule site-line__rule--right"></span>
  </p>
  <div class="front-band" aria-hidden="true">
    <span class="front-band__teal"></span>
    <span class="front-band__gold"></span>
  </div>
</section>

<section class="card card--back" aria-label="Card back">
  <div class="back-sweep" role="img" aria-label="Decorative teal and gold sweeping wave across the top of the card"></div>

  <h2 class="back-name">LORNA<br>MABBERY</h2>

  <span class="mark-ring" aria-hidden="true"></span>
  <p class="wordmark">
    <span class="wordmark__name">LORNA MABBERY</span>
    <span class="wordmark__sub">INTERIORS</span>
  </p>

  <ul class="contact">
    <li class="contact__item">
      <span>214-630-4182</span>
      <svg class="contact__icon" viewBox="0 0 16 16" aria-hidden="true"><path d="M2 6 C2 3 14 3 14 6 L11 7 L10 5 L6 5 L5 7 Z M4 8 L12 8 L13 13 L3 13 Z" fill="#0fa3a3"/></svg>
    </li>
    <li class="contact__item">
      <span>lorna.mabbery@quillpost.example</span>
      <svg class="contact__icon" viewBox="0 0 16 16" aria-hidden="true"><rect x="1" y="3" width="14" height="10" fill="#0fa3a3"/><path d="M1 3 L8 9 L15 3" fill="none" stroke="#1e1f20" stroke-width="1.4"/></svg>
    </li>
    <li class="contact__item">
      <span>lornamabberyinteriors.example</span>
      <svg class="contact__icon" viewBox="0 0 16 16" aria-hidden="true"><circle cx="8" cy="8" r="6.5" fill="#0fa3a3"/><path d="M1.5 8 H14.5 M8 1.5 V14.5 M8 1.5 C4 5 4 11 8 14.5 M8 1.5 C12 5 12 11 8 14.5" fill="none" stroke="#1e1f20" stroke-width="0.9"/></svg>
    </li>
  </ul>
</section>

</body>
</html>
```